Guaranteed Job - Sleek Sexy Business Card UV Spot

Im looking for a sleek and sexy business card, that resembles elite or VIP status status.
our business is corinvale.example
you can view our products on there, but our main audience for handing out our cards will be for people in the hospitality industry, so it will need to impress high management and CEO of hotels and restaurants, bars, clubs etc...
the card features will have UV spot on both sides, 400gsm stock. standard size.
Artwork should be 86 x 54mm + 2mm bleed = 90 x 58mm
it should have a nice "unique" uv spot pattern that highlights the card, not a repeated pattern, theres no originality there, and it will be disregarded.
The written material will be:
Corin Vale Hospitality College (logo)
Tobin Marsh
Director
Phone: 1300 615 737
Mobile: 0455 817 296
Email: info@corinvale.example
website: www.corinvale.example
I'm looking for originality here, i don't want just a simple stock card, want something that has a wow factor for people.
You will find the logo attached. you may invert the white to black words to suit the background as you please.
thank you and good luck
As a side note, ive received a lot of proposals, im too busy to give feedback to each and every one, so if i havent provided feedback for your design within 24 hours, then consider it not acceptable, and you could resubmit another design.
So far i have not seen any design that stood out for me, they all seem pretty generic. there nothing thats unique, i would figure for the amount that im offering, that people would put some more effort and creativity into the design.
so far over 200 designs submitted, and nothing i have seen looks very original, everything looks like a different variation of the same stuff, i said it very clearly i wanted something unique, the only thing that has come close to it so far is this one
Reason: Ive received alot of design concepts and i have reviewed everyone, but i havent had time to give feedback to every single one, only the ones that have interested me, if i havent responded, its because i havent found it good enough.
so far only a few design have been on par with what ive been looking for, an attractive eye popping design.
heres a few of them,
http://files.pixelbazaar.example/design_img/51736/62418/62418_2840915_51736_image.jpg
http://files.pixelbazaar.example/design_img/51736/68254/68254_2841377_51736_image.jpg
theyre, both unique and original, and eye catching, the only thing theyre missing is the sexyness.
if you still think you have some creativity left in your minds, then throw it on here.
Reason: Sorry guys for the delay, I was in a serious accident and out of commission for the past few months, I'm just slowly recovering now, please bare with me as i try to attend to this project, it may take me awhile as I have other projects that are on standby, I'm not 100% at the moment, so im extending the deadline for 2 weeks right now. Thanks for your patience.
Hospitality

```html
<!DOCTYPE html>
<html lang="en">
<head>
<meta charset="utf-8">
<title>Corin Vale Hospitality College – Business Card</title>
<link rel="stylesheet" href="https://fonts.googleapis.com/css2?family=Oswald:wght@500;600&family=Montserrat:wght@300;400;500&display=swap">
<style>
  :root {
    --canvas-bg: #2a2a2a;
    --card-bg: #1e1c1d;
    --card-edge: #141314;
    --accent-blue: #4aa3de;
    --name-grey: #c9c9c9;
    --text-light: #d4d4d4;
    --text-soft: #9a9a9a;
    --text-faint: #6e6e6e;
  }
  * { box-sizing: border-box; margin: 0; padding: 0; }
  html, body {
    width: 1200px;
    height: 900px;
    overflow: hidden;
    background: var(--canvas-bg);
  }
  .canvas {
    width: 1200px;
    height: 900px;
    display: flex;
    flex-direction: column;
    align-items: center;
    justify-content: center;
    gap: 44px;
  }
  .card {
    position: relative;
    width: 640px;
    height: 402px;
    background: var(--card-bg);
    border: 1px solid var(--card-edge);
    overflow: hidden;
  }

  /* Back side */
  .card-back .website {
    position: absolute;
    left: 52px;
    bottom: 78px;
    font-family: "Montserrat", sans-serif;
    font-weight: 300;
    font-size: 19px;
    letter-spacing: 0.14em;
    color: var(--text-faint);
  }

  /* Front side */
  .person {
    position: absolute;
    left: 52px;
    top: 78px;
  }
  .person-first,
  .person-last {
    display: block;
    font-family: "Oswald", sans-serif;
    font-weight: 600;
    font-size: 50px;
    line-height: 1.04;
    letter-spacing: 0.02em;
    text-transform: uppercase;
  }
  .person-first { color: var(--accent-blue); }
  .person-last { color: var(--name-grey); }
  .person-role {
    display: block;
    margin-top: 4px;
    font-family: "Montserrat", sans-serif;
    font-weight: 300;
    font-size: 24px;
    letter-spacing: 0.05em;
    color: var(--text-soft);
    text-transform: uppercase;
  }

  .contacts {
    position: absolute;
    left: 52px;
    bottom: 50px;
    list-style: none;
    font-family: "Montserrat", sans-serif;
    color: var(--text-light);
  }
  .contact-item {
    display: flex;
    align-items: center;
    gap: 10px;
    height: 30px;
    font-size: 19px;
    font-weight: 500;
  }
  .contact-item.email { font-weight: 300; }
  .contact-icon {
    width: 20px;
    height: 20px;
    flex: none;
    fill: none;
    stroke: var(--text-light);
    stroke-width: 1.6;
  }
  .contact-icon .solid { fill: var(--text-light); stroke: none; }

  .brand {
    position: absolute;
    right: 34px;
    top: 40px;
    width: 96px;
    height: 300px;
  }
  .brand-name {
    position: absolute;
    left: 50%;
    top: 50%;
    width: 300px;
    transform: translate(-50%, -50%) rotate(-90deg);
    display: flex;
    align-items: center;
    gap: 12px;
    font-family: "Oswald", sans-serif;
    font-weight: 500;
    font-size: 26px;
    line-height: 1.05;
    letter-spacing: 0.04em;
    text-transform: uppercase;
    color: var(--name-grey);
  }
  .brand-square {
    width: 22px;
    height: 22px;
    flex: none;
    background: var(--accent-blue);
  }
</style>
</head>
<body>
<main class="canvas">
  <section class="card card-back" aria-label="Card back">
    <p class="website">www.corinvale.example</p>
  </section>

  <section class="card card-front" aria-label="Card front">
    <div class="person">
      <span class="person-first">Tobin</span>
      <span class="person-last">Marsh</span>
      <span class="person-role">Director</span>
    </div>

    <ul class="contacts">
      <li class="contact-item phone">
        <svg class="contact-icon" viewBox="0 0 20 20" aria-hidden="true">
          <path class="solid" d="M5 2.5c1-.6 1.8-.3 2.2.6l1 2.3c.3.8 0 1.4-.6 1.8l-.9.6c.5 2 1.7 3.6 3.6 4.9l.9-.7c.6-.5 1.3-.5 1.9 0l1.9 1.5c.7.6.7 1.4 0 2.1l-1 1c-1.1 1-3 .8-5.1-.6C5.7 13.9 3.3 10.6 3 7.3c-.2-2 .6-3.8 2-4.8z"/>
        </svg>
        <span>1300 615 737</span>
      </li>
      <li class="contact-item mobile">
        <svg class="contact-icon" viewBox="0 0 20 20" aria-hidden="true">
          <rect x="5.5" y="2" width="9" height="16" rx="1.6"/>
          <rect class="solid" x="7.5" y="4.5" width="5" height="5"/>
          <circle class="solid" cx="10" cy="14.5" r="1.2"/>
        </svg>
        <span>0455 817 296</span>
      </li>
      <li class="contact-item email">
        <svg class="contact-icon" viewBox="0 0 20 20" aria-hidden="true">
          <rect x="1.5" y="4.5" width="17" height="11"/>
          <path d="M1.5 4.5l8.5 6.5 8.5-6.5"/>
        </svg>
        <span>info@corinvale.example</span>
      </li>
    </ul>

    <div class="brand">
      <div class="brand-name">
        <span class="brand-square" aria-hidden="true"></span>
        <span>Corin Vale Hospitality College</span>
      </div>
    </div>
  </section>
</main>
</body>
</html>
```